Veltrane Hand Sanitiser Spray Product Range for International Markets

Veltrane is a new Healthcare business launching a full product range of Anti-bacterial Hand Sanitiser Spray bottles in various sizes. We have a new logo which we believe differentiates us from the competition: Veltrane - Care That Goes Further
The Product Range will comprise two distinct product solution types:
- Anti-bacterial Hand Sanitisers - Alcohol based
- Anti-bacterial Hand Sanitisers - Sensitive Non Alcohol based
Bottle sizes will comprise a range containing:
100ml, 250ml, 500ml, 1ltr, 5ltr, 10ltr
Some bottles will have Pump Sprays
The Product labelling will be attractive front packaging label combined with strong product attributes and usage indicator cues.
As a Healthcare brand our logo design is light Green. We believe that this should be combined with blues and greens balanced to create contrast and strong stand-out on-shelf.
A review of competitor brands will show some similar colour cues, however as a Healthcare brand, the colour cues Green and White are synonymous with the sector. Many existing brands are very pragmatic in their label design. i.e. #it does what is says on the tin approach#. Our brand will need strong stand-out and strong aesthetic appeal too, since it will often be left in public view and around the home and office and therefore should look as attractive as possible. There will be other brand variants in the future and thought should be given to this too - with use of colour cues.
For Competitor indicators check-out the brands on Brisklot - Pine Hollow, Dermavell and others....Thank-you!

Target Market(s)

First: Female 25 - 65
Second: Male 25 - 65

Contact Information for Business Card

Garth L. Dunmore
CEO
Veltrane Healthcare Worldwide
'Care That Goes Further'
www.VeltraneHealthcare.example
E. gldunmore@veltranehealthcare.example
T. +44 7700 900318
T. +44 118 496072

Font styles to use
Sans Serif

Colors
34a7d7
33b8a4
add136
fbee3e
b768aa

```html
<!DOCTYPE html>
<html lang="en">
<head>
<meta charset="utf-8">
<title>Veltrane Anti-Bacterial Hand Sanitiser Labels</title>
<link rel="stylesheet" href="https://fonts.googleapis.com/css2?family=Montserrat:wght@400;500;600;700&display=swap">
<style>
  :root {
    --canvas: #f5f5f5;
    --white: #ffffff;
    --teal: #33b8a4;
    --lime: #add136;
    --ghost: #e2e2e2;
  }
  * { box-sizing: border-box; margin: 0; padding: 0; }
  html, body { width: 1000px; height: 1200px; overflow: hidden; }
  body {
    position: relative;
    background: var(--canvas);
    font-family: "Montserrat", sans-serif;
  }
  .label { position: absolute; overflow: hidden; background: var(--white); }
  .label-art { position: absolute; inset: 0; width: 100%; height: 100%; }
  .label > *:not(.label-art) { position: absolute; }

  .brand { display: flex; align-items: center; justify-content: center; }
  .brand-name { color: var(--lime); font-weight: 400; white-space: nowrap; }

  .product-title { color: var(--teal); font-weight: 600; text-align: center; line-height: 1.15; }
  .product-type { color: var(--teal); font-weight: 400; text-align: center; }

  .benefits { list-style: none; color: var(--teal); font-weight: 400; white-space: nowrap; }
  .benefits li { position: relative; }
  .benefits li::before {
    content: ""; position: absolute; border-radius: 50%; background: var(--lime);
  }
  .volume { color: var(--white); font-weight: 700; white-space: nowrap; }
  .body-copy { color: var(--white); font-size: 8.9px; line-height: 12.4px; letter-spacing: -0.1px; }

  /* Large 10 L label */
  .label--wide { left: 260px; top: 90px; width: 650px; height: 468px; }
  .label--wide .brand { left: 10px; top: 64px; width: 160px; height: 78px; }
  .label--wide .brand-name { font-size: 26px; }
  .label--wide .product-title { left: 262px; top: 68px; width: 340px; font-size: 34px; }
  .label--wide .product-type { left: 262px; top: 161px; width: 340px; font-size: 18px; }
  .label--wide .body-copy { left: 29px; top: 324px; width: 262px; }
  .label--wide .benefits { left: 341px; top: 329px; font-size: 21px; line-height: 26px; }
  .label--wide .benefits li::before { width: 7px; height: 7px; left: -21px; top: 9px; }
  .label--wide .volume { right: 22px; top: 434px; font-size: 16px; }

  /* Tall 100 ml label */
  .label--tall { left: 667px; top: 617px; width: 245px; height: 508px; border-radius: 14px; }
  .label--tall .brand { left: 0; top: 35px; width: 245px; height: 78px; }
  .label--tall .brand-name { font-size: 24px; }
  .label--tall .product-title { left: 0; top: 173px; width: 245px; font-size: 21px; }
  .label--tall .product-type { left: 0; top: 230px; width: 245px; font-size: 13px; }
  .label--tall .benefits { left: 49px; top: 378px; font-size: 15px; line-height: 18.5px; }
  .label--tall .benefits li::before { width: 6px; height: 6px; left: -15px; top: 6px; }
  .label--tall .volume { left: 0; width: 245px; text-align: center; top: 476px; font-size: 14px; }

  .stray-volume { position: absolute; left: 69px; top: 539px; color: var(--ghost); font-size: 14px; font-weight: 700; }

  .bottle-range {
    position: absolute; left: 110px; top: 605px; width: 425px; height: 522px;
    border-radius: 24px;
    background: linear-gradient(160deg, #fbfbfb 0%, #eeeeee 100%);
  }
</style>
</head>
<body>

  <section class="label label--wide" aria-label="10 litre front label">
    <svg class="label-art" viewBox="0 0 650 468" preserveAspectRatio="none" aria-hidden="true">
      <defs>
        <linearGradient id="wideBand" x1="0" y1="0" x2="1" y2="1">
          <stop offset="0" stop-color="#dcf2c9"/>
          <stop offset="1" stop-color="#a6e2d4"/>
        </linearGradient>
        <linearGradient id="wideWave" x1="0" y1="1" x2="1" y2="0">
          <stop offset="0" stop-color="#e6f5dc"/>
          <stop offset="1" stop-color="#f4fbf1"/>
        </linearGradient>
        <linearGradient id="wideSilver" x1="0" y1="0" x2="1" y2="0">
          <stop offset="0" stop-color="#e8e8e8"/>
          <stop offset="0.5" stop-color="#a9a9a9"/>
          <stop offset="1" stop-color="#d4d4d4"/>
        </linearGradient>
      </defs>
      <path d="M0 212 C 200 300, 460 290, 650 288 L 650 130 C 600 250, 470 270, 300 270 C 180 268, 80 240, 0 212 Z" fill="url(#wideWave)"/>
      <path d="M0 212 C 150 270, 420 285, 650 292 L 650 468 L 0 468 Z" fill="url(#wideBand)"/>
      <path d="M0 208 C 150 266, 420 283, 650 288 L 650 294 C 420 290, 150 276, 0 216 Z" fill="url(#wideSilver)"/>
      <path d="M0 302 L 650 302 L 650 304 L 0 304 Z" fill="#ffffff" opacity="0.35"/>
    </svg>
    <div class="brand"><span class="brand-name">Veltrane</span></div>
    <h1 class="product-title">ANTI-BACTERIAL<br>HAND SANITISER</h1>
    <p class="product-type">ALCOHOL BASED</p>
    <p class="body-copy">Lorem ipsum dolor sit amet, consectetuer adipiscing elit, sed diam nonummy nibh euismod tincidunt ut laoreet dolore magna aliquam erat volutpat. Ut wisi enim ad minim veniam, quis nostrud exerci tation ullamcorper suscipit lobortis nisl ut aliquip ex ea commodo consequat. Duis autem vel eum iriure dolor in hendrerit in vulputate velit esse molestie consequat, vel illum dolore eu feugiat Lorem ipsum dolor sit amet, consectetuer adipiscing elit,</p>
    <ul class="benefits">
      <li>Kills 99,9% of bateria</li>
      <li>Viruscidal</li>
      <li>Yeasticidal</li>
      <li>Fragance Free</li>
    </ul>
    <p class="volume">10 Ltr ℮</p>
  </section>

  <p class="stray-volume">100 ml ℮</p>

  <div class="bottle-range" role="img" aria-label="Product shot of the 10 litre jerrycan and 100 ml bottle wearing the labels"></div>

  <section class="label label--tall" aria-label="100 ml front label">
    <svg class="label-art" viewBox="0 0 245 508" preserveAspectRatio="none" aria-hidden="true">
      <defs>
        <linearGradient id="tallBand" x1="0" y1="0" x2="1" y2="1">
          <stop offset="0" stop-color="#d6f0c4"/>
          <stop offset="1" stop-color="#a8e2d6"/>
        </linearGradient>
        <linearGradient id="tallWave" x1="0" y1="1" x2="1" y2="0">
          <stop offset="0" stop-color="#e4f5d9"/>
          <stop offset="1" stop-color="#f7fcf4"/>
        </linearGradient>
        <linearGradient id="tallSilver" x1="0" y1="0" x2="1" y2="0">
          <stop offset="0" stop-color="#e4e4e4"/>
          <stop offset="0.5" stop-color="#a8a8a8"/>
          <stop offset="1" stop-color="#d0d0d0"/>
        </linearGradient>
      </defs>
      <path d="M0 268 C 60 320, 170 332, 245 332 L 245 140 C 225 260, 160 300, 90 300 C 50 300, 20 285, 0 268 Z" fill="url(#tallWave)"/>
      <path d="M0 268 C 50 312, 160 330, 245 334 L 245 508 L 0 508 Z" fill="url(#tallBand)"/>
      <path d="M0 264 C 50 308, 160 326, 245 328 L 245 334 C 160 332, 50 316, 0 272 Z" fill="url(#tallSilver)"/>
    </svg>
    <div class="brand"><span class="brand-name">Veltrane</span></div>
    <h2 class="product-title">ANTI-BACTERIAL<br>HAND SANITISER</h2>
    <p class="product-type">ALCOHOL BASED</p>
    <ul class="benefits">
      <li>Kills 99,9% of bateria</li>
      <li>Viruscidal</li>
      <li>Yeasticidal</li>
      <li>Fragance Free</li>
    </ul>
    <p class="volume">100 ml ℮</p>
  </section>

</body>
</html>
```